ashby paving works

Needs to have phone number 0412885107 and email marklowry@pavemail.com.au.
ABN 27613048852
name mark lowry

For all your concreting solutions
Excavation
Exposed & colour concrete
House & shed slabs
Driveways
Landing & steps

Contact Information for Business Card

ph 0412885107
email marklowry@pavemail.com.au.
ABN 27613048852
name mark lowry

```html
<!DOCTYPE html>
<html lang="en">
<head>
<meta charset="utf-8">
<title>Ashby Paving Works – Business Card</title>
<link rel="stylesheet" href="https://fonts.googleapis.com/css2?family=Montserrat:wght@500;700&family=Open+Sans:wght@400;600&display=swap">
<style>
  :root {
    --orange: #d4652a;
    --charcoal: #4d4d4f;
    --ink: #3a3a3c;
    --paper: #f6f6f6;
    --pattern-a: #ececec;
    --pattern-b: #dedede;
    --backdrop: #6d7074;
  }
  * { box-sizing: border-box; margin: 0; padding: 0; }
  html, body { width: 1200px; height: 800px; overflow: hidden; }
  body {
    background: var(--backdrop);
    font-family: "Open Sans", Arial, sans-serif;
    display: flex;
    flex-direction: column;
    align-items: center;
    justify-content: center;
    gap: 22px;
  }
  .card {
    position: relative;
    width: 620px;
    height: 354px;
    background: var(--paper);
    overflow: hidden;
    box-shadow: 0 6px 18px rgba(0,0,0,.25);
  }
  .card__texture {
    position: absolute; inset: 0;
    background: linear-gradient(135deg, var(--pattern-a) 0%, var(--pattern-b) 50%, var(--pattern-a) 100%);
    opacity: .7;
  }
  /* Front */
  .services {
    position: absolute; left: 26px; top: 30px;
    list-style: none;
  }
  .services li {
    display: table;
    background: var(--orange);
    color: var(--ink);
    font-size: 21px;
    line-height: 1.12;
    padding: 0 10px;
    margin-bottom: 1px;
  }
  .brand {
    position: absolute; left: 70px; top: 200px;
    display: flex; align-items: center; gap: 22px;
  }
  .brand__mark {
    width: 90px; height: 90px; background: var(--orange);
  }
  .brand__rule {
    width: 2px; height: 112px; background: var(--orange);
  }
  .brand__name {
    font-family: "Montserrat", Arial, sans-serif;
    font-weight: 700;
    font-size: 27px;
    color: var(--orange);
    letter-spacing: .5px;
    text-transform: uppercase;
  }
  .brand__phone {
    font-family: "Montserrat", Arial, sans-serif;
    font-weight: 500;
    font-size: 20px;
    color: var(--orange);
    letter-spacing: 3px;
    margin-top: 6px;
  }
  .brand__line {
    height: 2px; width: 280px; background: var(--charcoal); margin-top: 8px;
  }
  /* Back */
  .back-brand {
    position: absolute; left: 34px; top: 150px;
    display: flex; align-items: center; gap: 10px;
  }
  .back-brand__mark { width: 36px; height: 36px; background: var(--orange); }
  .back-brand__rule { width: 1px; height: 44px; background: var(--orange); }
  .back-brand__name {
    font-family: "Montserrat", Arial, sans-serif;
    font-weight: 700; font-size: 12px; color: var(--orange); text-transform: uppercase;
  }
  .back-brand__phone { font-size: 10px; color: var(--orange); letter-spacing: 1px; }
  .contact {
    position: absolute; right: 34px; top: 60px; width: 270px;
  }
  .contact__name {
    font-family: "Montserrat", Arial, sans-serif;
    font-weight: 700; font-size: 26px; color: var(--ink);
    text-transform: uppercase; letter-spacing: 1px;
  }
  .contact__abn {
    font-family: "Montserrat", Arial, sans-serif;
    font-weight: 700; font-size: 14px; color: var(--orange); margin-bottom: 18px;
  }
  .contact__row {
    display: flex; align-items: center; gap: 10px;
    height: 34px; border-radius: 17px 0 0 17px;
    padding-left: 4px; margin-bottom: 14px;
    font-size: 13px; color: #fff;
  }
  .contact__row--phone { background: var(--charcoal); }
  .contact__row--email { background: var(--orange); }
  .contact__icon {
    width: 26px; height: 26px; border-radius: 50%;
    background: #fff; display: flex; align-items: center; justify-content: center;
  }
</style>
</head>
<body>

  <section class="card card--front">
    <div class="card__texture" role="img" aria-label="Faint light grey interlocking geometric background pattern"></div>
    <ul class="services">
      <li>Driveways</li>
      <li>Excavation</li>
      <li>Landing &amp; steps</li>
      <li>House &amp; shed slabs</li>
      <li>Exposed &amp; colour concrete</li>
    </ul>
    <div class="brand">
      <div class="brand__mark"></div>
      <div class="brand__rule"></div>
      <div class="brand__text">
        <div class="brand__name">Ashby Paving Works</div>
        <div class="brand__line"></div>
        <div class="brand__phone">0412885107</div>
      </div>
    </div>
  </section>

  <section class="card card--back">
    <div class="card__texture" role="img" aria-label="Faint light grey interlocking geometric background pattern"></div>
    <div class="back-brand">
      <div class="back-brand__mark"></div>
      <div class="back-brand__rule"></div>
      <div>
        <div class="back-brand__name">Ashby Paving Works</div>
        <div class="back-brand__phone">0412885107</div>
      </div>
    </div>
    <div class="contact">
      <div class="contact__name">Mark Lowry</div>
      <div class="contact__abn">ABN: 27613048852</div>
      <div class="contact__row contact__row--phone">
        <span class="contact__icon">
          <svg width="14" height="14" viewBox="0 0 24 24"><path fill="#4d4d4f" d="M6.6 10.8a15 15 0 0 0 6.6 6.6l2.2-2.2c.3-.3.7-.4 1-.2 1.1.4 2.3.6 3.6.6.6 0 1 .4 1 1V20c0 .6-.4 1-1 1A17 17 0 0 1 3 4c0-.6.4-1 1-1h3.5c.6 0 1 .4 1 1 0 1.3.2 2.5.6 3.6.1.3 0 .7-.2 1z"/></svg>
        </span>
        0412885107
      </div>
      <div class="contact__row contact__row--email">
        <span class="contact__icon">
          <svg width="14" height="14" viewBox="0 0 24 24"><rect x="3" y="6" width="18" height="12" fill="none" stroke="#d4652a" stroke-width="2"/><path d="M3 6l9 7 9-7" fill="none" stroke="#d4652a" stroke-width="2"/></svg>
        </span>
        marklowry@pavemail.com.au
      </div>
    </div>
  </section>

</body>
</html>
```